Broschüre für Felgenmodelle
Zielgruppe
Wir sind Hersteller für Forged(geschmiedete) Felgen. Wir bieten 1-Teilige sowie 2-Teilige Schmiedefelgen. Unsere Kunden sind Leute mit Sportwägen, welche auf der Suche nach speziellen Felgen sind. Jede unserer Felgen ist eine Einzelanfertigung und wird auf Wunsch des Kunden angefertigt.
Aufgabenstellung
Die Broschüre sollte unsere verschiedenen Felgenmodelle Darstellen und unsere Preismodelle offenlegen. Es sollte nicht allzu kompliziert sein und die Felgendesigns sollten hervorstechen.
Bildmaterial download hier möglich: https://www.ablagekiste-beispiel.de/s/93qt5mzvenk2rwb/QHTp8uLxa3GcvN7kRJe0PmYTd?dl=0

```html
<!DOCTYPE html>
<html lang="de">
<head>
<meta charset="utf-8">
<title>Featherline Wheels – Broschüre</title>
<link rel="stylesheet" href="https://fonts.googleapis.com/css2?family=Cormorant+Garamond:wght@400;500;700&family=Raleway:wght@300;400;700&display=swap">
<style>
  :root {
    --page-dark: #0b0d10;
    --page-light: #f2f3f0;
    --panel: #ffffff;
    --ink-light: #f4f4f4;
    --ink-dark: #222222;
    --ink-heading: #3b3b3b;
    --accent-red: #9b2a2a;
    --tab-dark: #1d1b1b;
    --serif: "Cormorant Garamond", Georgia, serif;
    --sans: "Raleway", Arial, sans-serif;
  }
  * { margin: 0; padding: 0; box-sizing: border-box; }
  html, body { width: 1200px; height: 848px; overflow: hidden; background: #ffffff; }
  .spread { position: relative; width: 1200px; height: 848px; }

  /* left page */
  .page-left {
    position: absolute; left: 0; top: 0; width: 597px; height: 848px;
    background: var(--page-dark); color: var(--ink-light); overflow: hidden;
  }
  .page-left .backdrop {
    position: absolute; inset: 0;
    background:
      radial-gradient(ellipse 200px 170px at 400px 560px, rgba(110,92,40,.55), transparent 70%),
      radial-gradient(ellipse 260px 200px at 120px 160px, rgba(60,66,74,.45), transparent 70%),
      linear-gradient(170deg, #1b1f24 0%, #0c0e11 45%, #151515 80%, #0a0a0a 100%);
  }
  .page-left .content { position: absolute; inset: 0; }
  .title {
    position: absolute; left: 28px; top: 42px;
    font-family: var(--serif); font-weight: 400; font-size: 47px; letter-spacing: .5px; line-height: 1;
  }
  .subtitle {
    position: absolute; left: 29px; top: 96px;
    font-family: var(--sans); font-weight: 300; font-size: 22px; letter-spacing: .5px;
  }
  .section { position: absolute; width: 258px; }
  .section h2 {
    font-family: var(--serif); font-weight: 700; font-size: 11.5px; letter-spacing: .3px;
    text-transform: uppercase; margin-bottom: 16px;
  }
  .section p {
    font-family: var(--sans); font-weight: 300; font-size: 9.4px; line-height: 15.6px;
    text-align: justify; hyphens: auto; margin-bottom: 15px;
  }
  .section p.tight { margin-bottom: 0; }
  .page-num { position: absolute; top: 792px; font-family: var(--sans); font-size: 9px; font-weight: 700; }

  /* right page */
  .page-right {
    position: absolute; left: 597px; top: 0; width: 603px; height: 848px; background: var(--page-light);
  }
  .stripes { position: absolute; left: 388px; top: 0; }
  .kicker {
    position: absolute; left: 51px; top: 46px;
    font-family: var(--sans); font-weight: 700; font-size: 9.5px; line-height: 14px; color: var(--ink-dark);
  }
  .kicker .slashes { position: absolute; left: -2px; top: -1px; font-size: 14px; font-style: italic; }
  .kicker span.line { display: block; padding-left: 24px; }
  .kicker span.line + span.line { padding-left: 24px; }
  .panel { position: absolute; left: 75px; top: 96px; width: 519px; height: 562px; background: var(--panel); }
  .wheel { position: absolute; }
  .wheel-one {
    left: 120px; top: 107px; width: 170px; height: 168px;
    background: radial-gradient(circle at 50% 48%, #3a3c40 0%, #141517 45%, #0b0b0c 62%, #e9eaec 63%, #ffffff 72%);
  }
  .wheel-two {
    left: 361px; top: 111px; width: 175px; height: 165px;
    background: radial-gradient(circle at 50% 50%, #5b5f66 0%, #2a2d31 40%, #0d0e10 60%, #ffffff 66%);
  }
  .photo { position: absolute; overflow: hidden; }
  .photo-cast {
    left: 32px; top: 336px; width: 284px; height: 188px;
    background:
      radial-gradient(ellipse 90px 70px at 190px 130px, #8ea6be, transparent 75%),
      linear-gradient(135deg, #9a8f84 0%, #6f6a66 40%, #7c8a99 70%, #3d4048 100%);
  }
  .photo-case {
    left: 275px; top: 427px; width: 284px; height: 188px;
    background:
      radial-gradient(ellipse 130px 70px at 150px 110px, #2d2f36, transparent 80%),
      linear-gradient(160deg, #7a6048 0%, #4a3a2d 40%, #26262a 70%, #5a7d8a 100%);
  }
  .photo .badge {
    position: absolute; left: 4px; top: 4px; width: 22px; height: 22px; background: #f4f4f4;
  }
  .photo .tab {
    position: absolute; background: var(--tab-dark); color: #ffffff;
    font-family: var(--sans); font-weight: 400; font-size: 9.5px; letter-spacing: .3px;
    height: 30px; line-height: 30px;
  }
  .photo-cast .tab { left: 0; top: 32px; width: 74px; padding-left: 6px;
    clip-path: polygon(0 0, 82% 0, 100% 50%, 82% 100%, 0 100%); }
  .photo-case .tab { right: 0; top: 25px; width: 101px; padding-left: 10px; }
  .photo .caption {
    position: absolute; color: #ffffff; font-family: var(--sans); font-weight: 300; font-size: 9.5px; line-height: 14px;
  }
  .photo-cast .caption { left: 5px; top: 71px; }
  .photo-case .caption { right: 5px; top: 63px; text-align: right; }
  .claim {
    position: absolute; left: 86px; top: 664px;
    font-family: var(--serif); font-weight: 400; font-size: 38px; line-height: 42px;
    letter-spacing: 2px; color: var(--ink-heading); text-transform: uppercase;
  }
  .claim-shape { position: absolute; left: 496px; top: 648px; }
</style>
</head>
<body>
<div class="spread">

  <section class="page-left">
    <div class="backdrop" role="img" aria-label="Sportwagen mit goldfarbener geschmiedeter Felge im Dunkeln"></div>
    <div class="content">
      <h1 class="title">Leichtmetallräder</h1>
      <div class="subtitle">SWISS MADE</div>

      <div class="section" style="left:28px; top:172px;">
        <h2>Leichtmetallräder. Neu definiert.</h2>
        <p>Wir sind Featherline Wheels. Und wir sind stolz darauf, dass wir als Innovationsführer gelten, die neue Standards in der Branche setzen. Mit unseren Technologien tragen wir dazu bei, dass sich unser Industriezweig fortlaufend weiterentwickelt. Gute Wertarbeit ist eines der Aushängeschilder von uns und macht uns zu einem exzellenten Felgenhersteller.</p>
        <p>Schauen Sie sich unsere Bestseller an und kontaktieren Sie uns, wenn Sie Fragen zu unseren Produkten und Prozessen haben.</p>
      </div>

      <div class="section" style="left:28px; top:427px;">
        <h2>Unser Angebot</h2>
        <p>Bei Featherline Wheels werden alle Felgen aus geschmiedetem Aluminium 6061 T6 hergestellt, die mittels neuester Technologien weiterverarbeitet werden.</p>
        <p class="tight">Von der Ideenfindung bis zur finalen Ausführung erledigen wir alles. Wir sind sehr stolz auf unsere Arbeit. Wir sind davon überzeugt, dass Sie mit unseren Produkten zufrieden sein werden – so wie alle unsere bisherigen Kunden. Schauen Sie sich unsere Produktauswahl an.</p>
      </div>

      <div class="section" style="left:312px; top:172px;">
        <h2>Einteilige Felgen</h2>
        <p class="tight">Eine einteilige Felge besteht, wie der Name schon sagt, aus einem ganzen Teil. Der Felgenstern und das Felgenbett können nicht auseinander geschraubt werden. Deshalb sind Einteilige Felgen auch nur in einer Farbe Lackierbar.<br>Um die einteiligen Felgen spezieller zu machen, bieten wir auch an, vorne „Zierschrauben“ zu befestigen, damit sie einen zweiteiligen Look erhalten.</p>
      </div>

      <div class="section" style="left:312px; top:381px;">
        <h2>Zweiteilige Felgen</h2>
        <p class="tight">Bei den zweiteiligen Felgen wird der Stern und das Felgenbett unabhängig voneinander angefertigt. Der Stern und das Felgenbett werden nach deren Fertigstellung mittels Schrauben miteinander verbunden. Diese sind von vorne sichtbar, jedoch kann man die Felgen auch komplett ohne sichtbare Verschraubung bestellen.</p>
      </div>

      <div class="page-num" style="left:36px;">1</div>
    </div>
  </section>

  <section class="page-right">
    <svg class="stripes" width="215" height="28" viewBox="0 0 215 28" aria-hidden="true">
      <rect width="215" height="28" fill="#ffffff"/>
      <g fill="#9b2a2a">
        <polygon points="0,28 20,0 36,0 16,28"/>
        <polygon points="28,28 48,0 64,0 44,28"/>
        <polygon points="56,28 76,0 92,0 72,28"/>
        <polygon points="84,28 104,0 120,0 100,28"/>
        <polygon points="112,28 132,0 148,0 128,28"/>
        <polygon points="140,28 160,0 176,0 156,28"/>
        <polygon points="168,28 188,0 204,0 184,28"/>
        <polygon points="196,28 215,0 215,28"/>
      </g>
    </svg>

    <div class="kicker">
      <span class="slashes">//</span>
      <span class="line">SIE HABEN DIE WAHL</span>
      <span class="line">EINTEILIGE ODER ZWEITEILIGE RÄDER</span>
    </div>

    <div class="panel"></div>
    <div class="wheel wheel-one" role="img" aria-label="Einteilige schwarze Schmiedefelge"></div>
    <div class="wheel wheel-two" role="img" aria-label="Zweiteilige Schmiedefelge mit sichtbarer Verschraubung"></div>

    <div class="photo photo-cast" role="img" aria-label="Farbmuster aus Aluminium auf rostigem Untergrund">
      <div class="badge"></div>
      <div class="tab">GUSS</div>
      <div class="caption">aus hochfestem<br>Aluminium</div>
    </div>

    <div class="photo photo-case" role="img" aria-label="Holzkoffer mit farbigen Lackmustern">
      <div class="badge"></div>
      <div class="tab">SCHALTSCHRANK</div>
      <div class="caption">mit optimaler<br>Zugänglichkeit</div>
    </div>

    <div class="claim">Unser Anspruch<br>Ihr Vorteil</div>
    <svg class="claim-shape" width="98" height="120" viewBox="0 0 98 120" aria-hidden="true">
      <polygon points="22,0 98,0 98,120 22,120 0,60" fill="#1d1b1b"/>
    </svg>

    <div class="page-num" style="left:553px;">2</div>
  </section>

</div>
</body>
</html>
```